Web Design: Tovel Crowdfunding Platform

Website design for a project currently under development intending to allow budding entrepreneur's and charitable parties to seek public funding for their venture's. The platform is planned to operate in a similar way to ArtHive, with entrepreneur's and supporters. For details of how this sort of platform operates, you can check the brivopedia page [en.brivopedia.example/wiki/Crowd_funding].

An overview of the workflow;
1. Entrepreneur creates a venture.
2. Supporters discover venture and decide to support it.
3. Supporter commits to makes a payment commitment via some merchant gateway.
4. When the venture end time arrives, everyone involved is notified regarding the success or abandonment of the venture.
5. In the case of a successful funding raise;
5.1 Supporter payments are processed and approved or rejected.
5.2 Entrepreneur proceeds to contact all approved supporters in order to complete their pledges.

We have no existing branding for this product, so website design will include logo design. Something simple will most likely work best. We are using the name "Tovel Crowdunding" currently.

Will want to see your ideas for a few pages. In particular, the home page of course, a category/search page and a details page for a particular venture. We will attach screenshots of our working prototype, they give an idea of the layout we are currently working with. You will probably recognise the standard jQuery UI theme currently used. If you can design something nice within the jQuery UI framework, that's great, but it is probably too restricting.

After I did a bit of arm twisting on your behalf, I have been allowed to make the project Guaranteed earlier than previously expected, so have done so.

Appreciate your input!

Industry/Entity Type

Crowdfunding

Requirements
Should not have
• We would like to avoid loading/splash pages or anything that would slow down a user's initial experience. Minimise clicks from being new entrepreneur to getting a project going.

Avoid distracting animations [transition effects, appropriately used are effective].

```html
<!DOCTYPE html>
<html lang="en">
<head>
<meta charset="utf-8">
<title>Tovel Crowdfunding</title>
<link href="https://fonts.googleapis.com/css2?family=Ubuntu:wght@400;500&family=Open+Sans:ital,wght@0,400;0,600;1,400&display=swap" rel="stylesheet">
<style>
:root{
  --dark:#232323;
  --nav:#3a3a3a;
  --page:#ffffff;
  --orange:#e8820c;
  --orange-light:#f29a1e;
  --green:#8fd014;
  --bar-dark:#3b3b3b;
  --line:#c9c9c9;
  --text:#3c3c3c;
  --card-head:#efefef;
}
*{box-sizing:border-box;margin:0;padding:0}
html,body{width:836px;height:1200px;overflow:hidden;background:var(--page)}
body{position:relative;font-family:"Open Sans",Arial,sans-serif;color:var(--text)}
.abs{position:absolute}
.header{left:0;top:0;width:836px;height:90px;background:linear-gradient(#3a3a3a 0,#3a3a3a 5px,#2a2a2a 6px,#1f1f1f 100%)}
.brand{left:28px;top:38px;font-family:"Ubuntu",sans-serif;font-size:23px;color:#fff;font-weight:500;letter-spacing:.2px}
.user{right:30px;top:50px;display:flex;align-items:center;gap:8px;color:#fff;font-size:12.5px}
.logout{background:#111;border-radius:11px;padding:3px 12px;font-size:10px;color:#ddd}
.nav{left:0;top:90px;width:836px;height:36px;background:linear-gradient(#4a4a4a,#2f2f2f);display:flex}
.nav a{color:#fff;text-decoration:none;font-size:12px;line-height:36px;padding:0 22px;border-right:1px solid #222;box-shadow:1px 0 0 #555}
.nav a:first-child{padding-left:38px}
.nav a:last-of-type{border:none;box-shadow:none}
.search{right:38px;top:98px;width:162px;height:18px;background:#fff;border-radius:3px;font-size:9px;font-style:italic;color:#555;padding:2px 10px}
.search svg{position:absolute;right:5px;top:3px}
.subbar{left:0;top:126px;width:836px;height:49px;background:linear-gradient(#e6e6e6,#f7f7f7)}
.btn-dark{top:138px;height:26px;background:linear-gradient(#4a4a4a,#222);border-radius:3px;color:#eee;font-size:11.5px;line-height:26px;text-align:center;box-shadow:0 1px 2px rgba(0,0,0,.4)}
.hero{left:14px;top:188px;width:565px;height:200px;border-radius:4px;background:linear-gradient(120deg,#f1d27a 0%,#e6a84a 35%,#c9732a 60%,#f0c56a 100%)}
.box{border:1px solid var(--line);border-radius:4px;background:linear-gradient(#fff 60%,#f1f1f1)}
.box-title{font-family:"Ubuntu",sans-serif;font-size:15px;font-weight:400;color:#222}
.feat-text{left:12px;top:32px;font-size:8.6px;line-height:13px;color:#444;white-space:nowrap}
.feat-art{right:11px;top:19px;width:72px;height:66px;border-radius:4px;background:linear-gradient(#3ec21a 0,#2b9a10 35%,#d9c07a 65%,#b89a4a 100%)}
.email{left:12px;top:38px;width:208px;height:20px;background:#e8e8e8;border-radius:3px;font-size:8.6px;font-style:italic;color:#777;padding:3px 9px}
.subscribe{right:12px;top:66px;width:76px;height:21px;background:var(--orange);border-radius:3px;color:#fff;font-family:"Ubuntu",sans-serif;font-size:12px;line-height:21px;text-align:center}
.section-title{left:20px;top:404px;font-family:"Ubuntu",sans-serif;font-size:16px;font-weight:400;color:#222}
.section-rule{left:20px;top:429px;width:544px;height:2px;background:var(--orange)}
.venture{width:178px;height:185px;border:1px solid var(--line);border-radius:4px;background:#fff;overflow:hidden}
.venture h3{height:29px;background:var(--card-head);font-family:"Ubuntu",sans-serif;font-weight:400;font-size:13px;line-height:29px;text-align:center;color:#222}
.avatar{display:block;margin:6px auto 0;width:89px;height:75px;border:1px solid #ccc;border-radius:3px;background:linear-gradient(#ececec 0,#ececec 55%,#c6700a 56%,#b86508 100%)}
.venture p{margin:5px 0 0 9px;font-size:8.4px;line-height:14px;color:#444;height:42px;white-space:nowrap;letter-spacing:-.1px}
.progress{margin:4px 0 0 6px;width:161px;height:11px;border-radius:3px;background:var(--bar-dark);overflow:hidden}
.progress span{display:block;height:100%;background:linear-gradient(#a9e43a,var(--green))}
.panel{border:1px solid var(--line);border-radius:4px;background:#fff;overflow:hidden}
.panel-head{height:30px;background:linear-gradient(var(--orange-light),var(--orange));font-family:"Ubuntu",sans-serif;font-size:14px;color:#222;line-height:32px;padding-left:13px}
.video{left:3px;top:36px;width:235px;height:154px;background:#000}
.news-item{position:relative;height:101px;border-bottom:1px solid #ddd;background:linear-gradient(#fff 55%,#f0f0f0)}
.news-item.short{height:86px}
.cal{left:15px;top:16px;width:44px;height:42px;border-radius:2px;background:linear-gradient(#e8741e 0,#d1601a 25%,#e9eef4 26%,#d6dde6 100%)}
.news-item h4{position:absolute;left:73px;top:14px;font-family:"Ubuntu",sans-serif;font-weight:400;font-size:11px;color:#111}
.news-item p{position:absolute;left:73px;top:31px;font-size:8.6px;line-height:13px;color:#444;white-space:nowrap}
.news-item .more{position:absolute;left:73px;font-size:9.5px;color:#222}
.rule{height:1px;background:#cfcfcf}
.link-end{font-family:"Ubuntu",sans-serif;font-size:12px;color:#111}
.footer{left:0;top:1078px;width:836px;height:122px;background:linear-gradient(#222,#2c2c2c)}
.footer-links{left:25px;top:1095px;color:#fff;font-family:"Ubuntu",sans-serif;font-size:10.5px}
.footer-links span{margin:0 7px}
.copy{left:25px;top:1122px;color:#fff;font-family:"Ubuntu",sans-serif;font-size:10.5px}
</style>
</head>
<body>
<header class="abs header"></header>
<div class="abs brand">Tovel Crowdfunding</div>
<div class="abs user"><span>Milo |</span><span class="logout">Logout</span></div>

<nav class="abs nav">
  <a href="#">Home</a><a href="#">About Us</a><a href="#">Services</a><a href="#">Blog</a><a href="#">Forum</a><a href="#">How it works</a>
</nav>
<div class="abs search">search here..
  <svg width="11" height="11" viewBox="0 0 11 11"><circle cx="4.5" cy="4.5" r="3.3" fill="none" stroke="#222" stroke-width="1.5"/><line x1="7" y1="7" x2="10" y2="10" stroke="#222" stroke-width="1.8"/></svg>
</div>

<div class="abs subbar"></div>
<div class="abs btn-dark" style="left:24px;width:135px">Browse Categories</div>
<div class="abs btn-dark" style="left:188px;width:107px">Start A Venture</div>
<div class="abs btn-dark" style="left:320px;width:107px">Start Supporting</div>

<div class="abs hero" role="img" aria-label="Warm golden photo of banknotes and a brass compass"></div>

<section class="abs box" style="left:584px;top:189px;width:234px;height:99px">
  <h2 class="abs box-title" style="left:14px;top:8px">Featured Services</h2>
  <p class="abs feat-text">Brightwell Webworks is a<br>professional website design<br>company dedicated to provide<br>excellent services.</p>
  <div class="abs feat-art" role="img" aria-label="Green banker's desk lamp over documents"></div>
</section>
<section class="abs box" style="left:584px;top:289px;width:234px;height:99px">
  <h2 class="abs box-title" style="left:14px;top:10px">Newsletters sign up</h2>
  <div class="abs email">your email address</div>
  <div class="abs subscribe">Subscribe ›</div>
</section>

<h2 class="abs section-title">Popular Ventures</h2>
<div class="abs section-rule"></div>

<article class="abs venture" style="left:17px;top:441px"><h3>Venture 1</h3><div class="avatar" role="img" aria-label="Venture owner profile picture"></div><p>Our Website Design team give an<br>nforgettable impression on the custom<br>and the clients. We can assure you</p><div class="progress"><span style="width:62%"></span></div></article>
<article class="abs venture" style="left:202px;top:441px"><h3>Venture 2</h3><div class="avatar" role="img" aria-label="Venture owner profile picture"></div><p>Our Website Design team give an<br>nforgettable impression on the custom<br>and the clients. We can assure you</p><div class="progress"><span style="width:62%"></span></div></article>
<article class="abs venture" style="left:387px;top:441px"><h3>Venture 3</h3><div class="avatar" role="img" aria-label="Venture owner profile picture"></div><p>Our Website Design team give an<br>nforgettable impression on the custom<br>and the clients. We can assure you</p><div class="progress"><span style="width:62%"></span></div></article>

<article class="abs venture" style="left:17px;top:638px"><h3>Venture 4</h3><div class="avatar" role="img" aria-label="Venture owner profile picture"></div><p>Our Website Design team give an<br>nforgettable impression on the custom<br>and the clients.</p><div class="progress"><span style="width:62%"></span></div></article>
<article class="abs venture" style="left:202px;top:638px"><h3>Venture 5</h3><div class="avatar" role="img" aria-label="Venture owner profile picture"></div><p>Our Website Design team give an<br>nforgettable impression on the custom<br>and the clients.</p><div class="progress"><span style="width:62%"></span></div></article>
<article class="abs venture" style="left:387px;top:638px"><h3>Venture 6</h3><div class="avatar" role="img" aria-label="Venture owner profile picture"></div><p>Our Website Design team give an<br>nforgettable impression on the custom<br>and the clients.</p><div class="progress"><span style="width:62%"></span></div></article>

<article class="abs venture" style="left:14px;top:835px"><h3>Venture 7</h3><div class="avatar" role="img" aria-label="Venture owner profile picture"></div><p>Our Website Design team give an<br>nforgettable impression on the custom<br>and the clients.</p><div class="progress"><span style="width:62%"></span></div></article>
<article class="abs venture" style="left:200px;top:841px"><h3>Venture 8</h3><div class="avatar" role="img" aria-label="Venture owner profile picture"></div><p>Our Website Design team give an<br>nforgettable impression on the custom<br>and the clients.</p><div class="progress"><span style="width:62%"></span></div></article>
<article class="abs venture" style="left:385px;top:835px"><h3>Venture 9</h3><div class="avatar" role="img" aria-label="Venture owner profile picture"></div><p>Our Website Design team give an<br>nforgettable impression on the custom<br>and the clients.</p><div class="progress"><span style="width:62%"></span></div></article>

<section class="abs panel" style="left:579px;top:400px;width:243px;height:203px">
  <div class="panel-head">Our Video</div>
  <div class="abs video">
    <svg width="235" height="154" viewBox="0 0 235 154">
      <rect x="92" y="56" width="54" height="34" rx="3" fill="#2a2a2a" stroke="#444"/>
      <polygon points="114,66 114,80 126,73" fill="#555"/>
      <line x1="12" y1="140" x2="226" y2="140" stroke="#ddd" stroke-width="1.2"/>
      <circle cx="22" cy="140" r="4.5" fill="#fff"/>
    </svg>
  </div>
</section>

<section class="abs panel" style="left:579px;top:610px;width:243px;height:422px">
  <div class="panel-head">Latest News</div>
  <div class="news-item"><div class="abs cal" role="img" aria-label="Calendar icon"></div><h4>News headline here</h4><p>Brightwell Webworks is a professional<br>website design company dedicated to<br>provide excellent services.</p><span class="more" style="top:75px">read more ›</span></div>
  <div class="news-item"><div class="abs cal" role="img" aria-label="Calendar icon"></div><h4>News headline here</h4><p>Brightwell Webworks is a professional<br>website design company dedicated to<br>provide excellent services.</p><span class="more" style="top:75px">read more ›</span></div>
  <div class="news-item short"><div class="abs cal" role="img" aria-label="Calendar icon"></div><h4>News headline here</h4><p>Brightwell Webworks is a professional<br>website design company</p><span class="more" style="top:61px">read more ›</span></div>
  <div class="news-item short" style="border:none"><div class="abs cal" role="img" aria-label="Calendar icon"></div><h4>News headline here</h4><p>Brightwell Webworks is a professional<br>website design company</p><span class="more" style="top:61px">read more ›</span></div>
</section>

<div class="abs rule" style="left:14px;top:1043px;width:547px"></div>
<div class="abs rule" style="left:579px;top:1043px;width:243px"></div>
<div class="abs link-end" style="left:525px;top:1047px">view all</div>
<div class="abs link-end" style="left:769px;top:1046px">read more</div>

<footer class="abs footer"></footer>
<div class="abs footer-links">Contact us<span>|</span>Terms of Use<span>|</span>Privacy and cookie policy<span>|</span>Sitemap<span>|</span>FAQ</div>
<div class="abs copy">© Company Name &nbsp;|&nbsp; All right reserved</div>
</body>
</html>
```